Cercle doré
Zielgruppe
Branche: klassische Musik; Musikgruppe: Klaviertrio (Geige, Cello, Klavier) Gesucht wird ein Flyer, den wir zur Aussendarstellung nutzen können. Zielgruppe sind Veranstalter von klassisch-konservativen Konzerten. Inhalt: Fotos der 3 MusikerInnen, 3x Porträtfoto, 1 Gesamtfoto, 3 Biografien, 1 Text zu unserem Klaviertrio. Der Flyer soll hauptsächlich per mail versandt werden, eine geringe Stückzahl soll ausgedruckt werden.
Format: DIN lang105 QUER !! 210 x 105 mm Vorder- und Rückseite ODER:
DIN lang 105 quer Einbruchfalz
Aufgabenstellung
Das Klaviertrio heisst "Cercle doré", wir spielen hauptsächlich klassisch-romantische Werke. Das Design sollte klassisch-romantisch, aber nicht zu verschnörkelt sein.

```html
<!DOCTYPE html>
<html lang="de">
<head>
<meta charset="utf-8">
<title>Cercle doré – Flyer</title>
<link href="https://fonts.googleapis.com/css2?family=Cormorant+Garamond:wght@500&family=PT+Sans+Narrow:wght@400;700&family=Source+Sans+3:wght@400&display=swap" rel="stylesheet">
<style>
  :root {
    --page: #ffffff;
    --label: #6b6b6b;
    --rose-light: #f2b3a6;
    --rose-mid: #e5a595;
    --rose-soft: #eaa99a;
    --hair-auburn: #8a3a2c;
    --hair-blonde: #d99a6a;
    --skin: #e9a08c;
    --dress-slate: #4a3a3c;
    --dress-wine: #8a2e2c;
    --suit-dark: #3a1f24;
    --ice-blue: #c6e6f6;
    --bio-text: #fbe9e4;
    --logo-dark: #5a1a24;
  }
  * { margin: 0; padding: 0; box-sizing: border-box; }
  html, body { width: 1200px; height: 646px; overflow: hidden; background: var(--page); }
  .canvas { position: relative; width: 1200px; height: 646px; }

  .side { position: absolute; top: 135px; height: 395px; overflow: hidden; }
  .side--front { left: 33px; width: 550px; background: linear-gradient(180deg, #e9a89a 0%, var(--rose-light) 100%); }
  .side--back { left: 606px; width: 552px; display: flex; }

  .label {
    position: absolute; top: 530px;
    font-family: "Source Sans 3", sans-serif; font-size: 23px; color: var(--label);
  }
  .label--front { left: 34px; }
  .label--back { left: 609px; }

  /* musician placeholders: head-and-shoulder zones in photo tones */
  .figure {
    position: absolute; bottom: 0;
    border-radius: 48% 48% 0 0 / 30% 30% 0 0;
  }
  .figure--cellist-front {
    left: 0; width: 230px; top: 8px;
    background: linear-gradient(180deg, var(--hair-auburn) 0%, var(--skin) 18%, var(--skin) 40%, var(--dress-slate) 58%, #2e2628 100%);
  }
  .figure--pianist-front {
    left: 195px; width: 190px; top: 20px;
    background: linear-gradient(180deg, #5a2a24 0%, var(--skin) 14%, var(--skin) 30%, var(--suit-dark) 44%, #241418 100%);
  }
  .figure--violinist-front {
    left: 360px; width: 190px; top: 92px;
    background: linear-gradient(180deg, var(--hair-blonde) 0%, var(--skin) 28%, #b86a52 55%, var(--dress-wine) 75%, #4a1a1e 100%);
  }

  .front-name {
    position: absolute; left: 0; right: 0; top: 424px;
    font-family: "Cormorant Garamond", serif; font-weight: 500;
    font-size: 52px; letter-spacing: 5px; text-transform: uppercase;
    color: var(--ice-blue); text-align: center; white-space: nowrap;
  }
  .side--front .front-name { top: 289px; }

  .member { position: relative; height: 100%; }
  .member--cellist { width: 183px; background: var(--rose-mid); }
  .member--violinist { width: 184px; background: var(--rose-light); }
  .member--pianist { width: 185px; background: var(--rose-soft); }

  .figure--cellist-back {
    left: 2px; width: 150px; top: 168px;
    background: linear-gradient(180deg, var(--hair-auburn) 0%, var(--skin) 18%, var(--skin) 36%, var(--dress-slate) 55%, #c9784e 75%, #a85a38 100%);
  }
  .figure--violinist-back {
    left: 10px; width: 140px; top: 155px;
    background: linear-gradient(180deg, var(--hair-blonde) 0%, var(--skin) 20%, var(--skin) 40%, var(--dress-wine) 60%, #6a2024 100%);
  }
  .figure--pianist-back {
    left: 14px; width: 160px; top: 152px;
    background: linear-gradient(180deg, #4a2420 0%, var(--skin) 14%, var(--skin) 30%, var(--suit-dark) 42%, #261418 100%);
  }

  .bio {
    position: absolute; left: 10px; top: 15px;
    font-family: "PT Sans Narrow", sans-serif; color: var(--bio-text);
    font-size: 10.5px; line-height: 13.2px;
  }
  .bio-name { font-weight: 700; font-size: 11px; }

  .back-name {
    position: absolute; left: 164px; top: 478px; width: 230px;
    font-family: "Cormorant Garamond", serif; font-weight: 500;
    font-size: 25px; letter-spacing: 1.5px; text-transform: uppercase;
    color: var(--logo-dark); text-align: center; white-space: nowrap;
  }
  .side--back .back-name { top: 343px; }
</style>
</head>
<body>
<main class="canvas">
  <section class="side side--front" role="img" aria-label="Gruppenfoto: Cellistin, Pianist und Geigerin mit Cello und Geige vor rosa Hintergrund">
    <div class="figure figure--cellist-front"></div>
    <div class="figure figure--pianist-front"></div>
    <div class="figure figure--violinist-front"></div>
    <p class="front-name">Cercle doré</p>
  </section>
  <p class="label label--front">Vorderseite</p>

  <section class="side side--back">
    <article class="member member--cellist">
      <div class="figure figure--cellist-back" role="img" aria-label="Porträt der Cellistin mit ihrem Cello"></div>
      <div class="bio">
        <p class="bio-name">CLAIRE</p>
        <p>Aabvummmn Lorrbbbc</p><p>Efgnm Obssturz</p><p>Cvdopcsüümktlrk</p><p>Wenkuolpi</p>
      </div>
    </article>
    <article class="member member--violinist">
      <div class="figure figure--violinist-back" role="img" aria-label="Porträt der Geigerin im roten Kleid mit Geige"></div>
      <div class="bio">
        <p class="bio-name">CLAIRE</p>
        <p>Aabvummmn Lorrbbbc</p><p>Efgnm Obssturz</p><p>Cvdopcsüümktlrk</p><p>Wenkuolpi</p>
      </div>
    </article>
    <article class="member member--pianist">
      <div class="figure figure--pianist-back" role="img" aria-label="Porträt des Pianisten im Sakko am Flügel"></div>
      <div class="bio">
        <p class="bio-name">CLAIRE</p>
        <p>Aabvummmn Lorrbbbc</p><p>Efgnm Obssturz</p><p>Cvdopcsüümktlrk</p><p>Wenkuolpi</p>
      </div>
    </article>
    <p class="back-name">Cercle doré</p>
  </section>
  <p class="label label--back">Rückseite</p>
</main>
</body>
</html>
```